Wordpress design for my private practice website - Psychotherapist

I would like a simple, clean, and elegant design for my private practice website. I work with both adults and children so I'd like it to appeal to both. However, since parents make the choice as to where to send their child for therapy, I want it to appeal to adults more. I would like the pictures on the site to have a calming effect - maybe using sand and water and rocks. I am attaching files with my company logo. I would also like my name incorporated into the header - Rosalind Vantreece, LCSW, Registered Play Therapist. I've also uploaded a picture of myself for my About Page.

I like the design of these 2 website and want something similar:
www.drmaribelostrand.com
www.harrowgate-lisk.com

I would like a home page that highlights a calming graphic across the entire top of the page as well as my practice logo and my name.

I'd like a link to social media sites on the top of the homepage - facebook, pinterest.

I want a simple bar across the top with the following tabs:
Home
About Me (subtabs Who I Am, Specialties and Approach)
Counseling Services (subtabs Individual Counseling, Play Therapy, Sandplay Therapy,)
Fees
FAQs
Contact Me (would love this to be a fill in the blank contact form that sends info to my email address - should include name, phone number, email and a comment box for more information requested)
Blog (this will link with another wordpress blog)

Target Market(s)

Parents of children under age 12 with behavioral problems or are dealing with the breakup of their family through divorce - looking for someone to work with their young child. I also work with Adults that are overwhelmed and worried - often women that have many life stressors and are feeling burnt out on life and meeting everyone's needs. Families going through some type of trauma, including divorce or grief work. I also work with individuals going through a transition of religious beliefs - often exiting the religion of their youth and undergoing a crisis of faith at midlife.

Industry/Entity Type

Mental Health

Contact Information for Business Card

Rosalind Vantreece, LCSW
Registered Play Therapist
4815 Bellhaven Court
Idaho Falls, Idaho 83404
(208)555-7162
www.stillbrookwellness.com

On the opposite side, I'd like an appointment reminder area - with the following text:

Your next appointment is
_____/______/______ at ______am/pm
Please give 24 hrs notice if you need to cancel your appointment.

Coding

Coded - Design and coding required

Number of Pages Required

5+ page

Font styles to use
Sans Serif

Colors
33a6d7
9bcb3c
0355a3

Requirements
Must have
• I'd like it to be a wordpress site. I'm such a newby at web design - but I need to be able to add content and manage the site myself once it is up and running.
Nice to have
• I like the design of these 2 websites and want something similar:
• www.drmaribelostrand.com
• www.harrowgate-lisk.com
• They are clean, easy to navigate and calming.
Should not have
• Should not look like a childcare website.

```html
<!DOCTYPE html>
<html lang="en">
<head>
<meta charset="utf-8">
<title>Stillbrook – Rosalind Vantreece</title>
<link href="https://fonts.googleapis.com/css2?family=Open+Sans:ital,wght@0,400;0,600;0,700;1,400&display=swap" rel="stylesheet">
<style>
  :root {
    --ink: #111111;
    --text: #555555;
    --muted: #7a7a7a;
    --blue: #1a73a8;
    --icon-blue: #2c7fb0;
    --teal: #1aa8ad;
    --footer: #1e88b5;
    --white: #ffffff;
  }
  * { box-sizing: border-box; margin: 0; padding: 0; }
  html, body { width: 1200px; height: 2359px; overflow: hidden; background: var(--white); }
  body { position: relative; font-family: "Open Sans", Verdana, sans-serif; color: var(--text); }
  .abs { position: absolute; }

  /* Header bar */
  .site-header { position: absolute; left: 0; top: 0; width: 1200px; height: 64px; background: var(--white); }
  .brand { left: 236px; top: 21px; display: flex; align-items: center; gap: 8px; font-size: 14px; font-weight: 700; color: var(--ink); }
  .brand-dot { width: 12px; height: 12px; border-radius: 50%; background: var(--icon-blue); }
  .main-nav a { position: absolute; top: 24px; font-size: 12.5px; font-weight: 600; color: #555; text-decoration: none; }
  .nav-contact { color: var(--blue) !important; }

  /* Hero */
  .hero { left: 0; top: 64px; width: 1200px; height: 354px;
    background:
      radial-gradient(ellipse 300px 120px at 150px 70px, rgba(240,160,70,.55), transparent 70%),
      radial-gradient(ellipse 400px 150px at 900px 60px, rgba(230,150,70,.35), transparent 70%),
      linear-gradient(180deg, #4c5566 0%, #5b5e66 35%, #8a6640 60%, #c4843e 78%, #6b4a2c 100%); }
  .hero-title { left: 0; width: 1200px; top: 146px; text-align: center; font-size: 36px; font-weight: 700; color: var(--white); letter-spacing: .5px; }
  .hero-rule { left: 433px; top: 193px; width: 336px; height: 2px; background: var(--white); }
  .hero-name { left: 0; width: 1200px; top: 207px; text-align: center; font-size: 16px; color: var(--white); }
  .hero-role { left: 0; width: 1200px; top: 237px; text-align: center; font-size: 11px; color: var(--white); }
  .hero-button { left: 550px; top: 274px; width: 103px; height: 28px; border: 2px solid var(--white); color: var(--white); font-size: 11px; font-weight: 700; text-align: center; line-height: 24px; }
  .social-dot { width: 17px; height: 17px; border-radius: 50%; background: var(--white); }

  /* Services */
  .section-title { font-size: 26px; font-weight: 600; color: var(--ink); }
  .services-title { left: 0; width: 1200px; top: 496px; text-align: center; }
  .service { width: 140px; text-align: center; font-size: 11.5px; line-height: 14px; color: var(--ink); }
  .service svg { display: block; margin: 0 auto 14px; }
  .services-text { left: 385px; top: 708px; width: 430px; text-align: center; font-size: 12.5px; line-height: 20px; }

  /* Blog */
  .blog-photo { left: 0; width: 530px; height: 225px; }
  .photo-leaf { top: 890px; background: linear-gradient(100deg, #9cbb4a 0%, #c6dc7a 40%, #e6efc4 70%, #b5d06a 100%); }
  .photo-hiker { top: 1147px; background: linear-gradient(180deg, #dfeef6 0%, #c6e0ea 45%, #93b5b0 60%, #4f7f4c 85%, #3d6a3a 100%); }
  .photo-notch { right: 0; top: 102px; width: 0; height: 0; border-top: 10px solid transparent; border-bottom: 10px solid transparent; border-right: 10px solid var(--white); }
  .blog-title { left: 604px; top: 880px; }
  .post-date { font-size: 13px; font-style: italic; color: var(--muted); }
  .post-title { width: 380px; font-size: 15px; font-weight: 700; line-height: 19px; color: var(--ink); }
  .post-text { width: 370px; font-size: 12.5px; line-height: 20px; }
  .blog-link { left: 601px; top: 1358px; font-size: 14px; font-weight: 700; color: var(--blue); letter-spacing: .5px; }

  /* FAQ */
  .faq-title { left: 233px; top: 1460px; }
  .faq-q { width: 310px; font-size: 12.5px; line-height: 20px; font-style: italic; color: var(--muted); }
  .faq-a { width: 300px; font-size: 12.5px; line-height: 20px; color: #444; }

  /* Lake band */
  .lake-band { left: 0; top: 1749px; width: 1200px; height: 258px;
    background: linear-gradient(180deg, #8dc4df 0%, #c8c3a6 18%, #b9b28e 45%, #3fa4b6 62%, #1d8fa8 100%); }

  /* Closing call */
  .closing-text { left: 374px; top: 2076px; width: 452px; text-align: center; font-size: 12.5px; line-height: 20px; color: #444; }
  .closing-button { left: 540px; top: 2155px; width: 124px; height: 28px; background: var(--teal); color: var(--white); font-size: 11.5px; font-weight: 700; text-align: center; line-height: 28px; }

  /* Footer */
  .site-footer { left: 0; top: 2256px; width: 1200px; height: 103px; background: var(--footer); }
  .footer-nav a { position: absolute; top: 43px; font-size: 12px; font-weight: 700; color: var(--white); text-decoration: none; }
</style>
</head>
<body>

<header class="site-header">
  <div class="abs brand"><span class="brand-dot"></span>Stillbrook</div>
  <nav class="main-nav">
    <a style="left:426px">About me</a>
    <a style="left:520px">Counselling Services</a>
    <a style="left:679px">Fees</a>
    <a style="left:737px">FAQ`S</a>
    <a class="nav-contact" style="left:893px">Contact me</a>
  </nav>
</header>

<section class="abs hero" role="img" aria-label="Close-up of dark pebbles on wet sand with warm glowing light at sunset"></section>
<h1 class="abs hero-title">STILLBROOK</h1>
<div class="abs hero-rule"></div>
<p class="abs hero-name">Rosalind Vantreece</p>
<p class="abs hero-role">LCSW, Registered Play Therapist</p>
<div class="abs hero-button">ABOUT ME</div>
<span class="abs social-dot" style="left:579px;top:377px"></span>
<span class="abs social-dot" style="left:605px;top:377px"></span>

<h2 class="abs section-title services-title">Counselling Services</h2>

<div class="abs service" style="left:353px;top:563px">
  <svg width="70" height="68" viewBox="0 0 70 68" fill="none" stroke="var(--icon-blue)" stroke-width="2.2" stroke-linejoin="round">
    <path d="M4 14h14a7 7 0 1 1 12 0h14v14a7 7 0 1 1 0 12v14H30a7 7 0 1 0-12 0H4V40a7 7 0 1 0 0-12z"/>
  </svg>
  individual<br>counseling
</div>
<div class="abs service" style="left:534px;top:563px">
  <svg width="70" height="68" viewBox="0 0 70 68" fill="none" stroke="var(--icon-blue)" stroke-width="2.2" stroke-linejoin="round">
    <path d="M64 4C46 6 30 16 22 34l12 12c18-8 28-24 30-42z"/>
    <circle cx="44" cy="24" r="5"/>
    <path d="M22 34l-10 2-6 8 12-1M34 46l-2 10-8 6 1-12"/>
    <path d="M16 48c-4 2-8 8-8 12 4 0 10-4 12-8"/>
  </svg>
  play<br>therapy
</div>
<div class="abs service" style="left:712px;top:561px">
  <svg width="70" height="68" viewBox="0 0 70 68" fill="none" stroke="var(--icon-blue)" stroke-width="2.2" stroke-linecap="round">
    <path d="M8 22c8-6 14-6 22 0s14 6 22 0 10-4 12-2"/>
    <path d="M8 36c8-6 14-6 22 0s14 6 22 0 10-4 12-2"/>
    <path d="M8 50c8-6 14-6 22 0s14 6 22 0 10-4 12-2"/>
  </svg>
  sandplay<br>therapy
</div>

<p class="abs services-text">Lorem ipsum dolor sit amet, consectetur adipiscing elit. Donec sodales mi id augue fermentum maximus. Vivamus feugiat odio nec enim lobortis tempor at sit amet neque</p>

<div class="abs blog-photo photo-leaf" role="img" aria-label="Butterfly resting on a green leaf with a water droplet"><span class="abs photo-notch"></span></div>
<div class="abs blog-photo photo-hiker" role="img" aria-label="Hiker seated on a rock overlooking misty green hills"><span class="abs photo-notch"></span></div>

<h2 class="abs section-title blog-title">Latest Blog Posts</h2>

<p class="abs post-date" style="left:601px;top:955px">22 February 2016 | individual counseling</p>
<h3 class="abs post-title" style="left:601px;top:997px">Lorem ipsum dolor sit amet, consectetur adipiscing elit onec sodales</h3>
<p class="abs post-text" style="left:601px;top:1060px">Vivamus feugiat odio nec enim lobortis tempor at sit amet neque. Mauris ac ultricies massa. Nullam vel nisl erat. Aliquam condimentum</p>

<p class="abs post-date" style="left:601px;top:1164px">22 February 2016 | individual counseling</p>
<h3 class="abs post-title" style="left:601px;top:1205px">Lorem ipsum dolor sit amet, consectetur adipiscing elit onec sodales</h3>
<p class="abs post-text" style="left:601px;top:1268px">Vivamus feugiat odio nec enim lobortis tempor at sit amet neque. Mauris ac ultricies massa. Nullam vel nisl erat. Aliquam condimentum</p>

<a class="abs blog-link">GO TO BLOG</a>

<h2 class="abs section-title faq-title">FAQ`S</h2>
<svg class="abs" style="left:176px;top:1578px" width="14" height="26" viewBox="0 0 14 26" fill="none" stroke="var(--icon-blue)" stroke-width="1.6"><path d="M12 2L2 13l10 11"/></svg>
<svg class="abs" style="left:1009px;top:1578px" width="14" height="26" viewBox="0 0 14 26" fill="none" stroke="var(--icon-blue)" stroke-width="1.6"><path d="M2 2l10 11L2 24"/></svg>

<p class="abs faq-q" style="left:236px;top:1536px">Vivamus feugiat odio nec enim lobortis tempor at sit amet neque?</p>
<p class="abs faq-a" style="left:236px;top:1599px">Vivamus feugiat odio nec enim lobortis tempor at sit amet neque. Mauris ac ultricies massa. Nullam vel nisl erat. Aliquam condimentum</p>
<p class="abs faq-q" style="left:657px;top:1536px">Vivamus feugiat odio nec enim lobortis tempor at sit amet neque?</p>
<p class="abs faq-a" style="left:657px;top:1599px">Vivamus feugiat odio nec enim lobortis tempor at sit amet neque. Mauris ac ultricies massa. Nullam vel nisl erat. Aliquam condimentum</p>

<div class="abs lake-band" role="img" aria-label="Smooth pale boulders reflected in calm turquoise lake water"></div>

<p class="abs closing-text">Vivamus feugiat odio nec enim lobortis tempor at sit amet neque. Mauris ac ultricies massa. Nullam vel nisl erat. Aliquam condimentum</p>
<div class="abs closing-button">CONTACT ME</div>

<footer class="abs site-footer">
  <nav class="footer-nav">
    <a style="left:236px">About me</a>
    <a style="left:326px">Counselling Services</a>
    <a style="left:480px">Fees</a>
    <a style="left:537px">FAQ`S</a>
    <a style="left:600px">Contact me</a>
  </nav>
  <span class="abs social-dot" style="left:915px;top:42px"></span>
  <span class="abs social-dot" style="left:942px;top:42px"></span>
</footer>

</body>
</html>
```